Tailbrook Website Design

Need a website for a Dog Grooiming business. Please make it simular to these:

https://www.furvanto.com
https://haulnorix.com
https://meadowpetrin.com
https://www.drivelumo.com/search/

```html
<!DOCTYPE html>
<html lang="en">
<head>
<meta charset="utf-8">
<title>Tailbrook – Doorstep Dog Grooming</title>
<link rel="stylesheet" href="https://fonts.googleapis.com/css2?family=Montserrat:wght@400;500;600;700&family=Dancing+Script:wght@700&display=swap">
<style>
:root{
  --blue:#3f8cf0;
  --blue-deep:#1e63e0;
  --sky:#62d3fb;
  --purple:#8c6cf2;
  --violet:#a024d8;
  --ink:#111;
  --gray:#7b7b7b;
  --soft:#f4f6fb;
  --white:#fff;
}
*{margin:0;padding:0;box-sizing:border-box}
html,body{width:1200px;height:3826px;overflow:hidden;background:var(--white)}
body{position:relative;font-family:"Montserrat",sans-serif;color:var(--ink)}
.abs{position:absolute}
svg.abs{display:block}

/* header */
.brand{left:80px;top:72px;display:flex;align-items:center;gap:8px;font-weight:700;font-size:26px;color:var(--ink)}
.brand .dot{width:14px;height:14px;border-radius:50%;background:var(--blue)}
.nav{left:238px;top:100px;display:flex;gap:0;font-size:16px}
.nav a{color:var(--ink);text-decoration:none;margin-right:42px}
.btn-outline{left:861px;top:90px;width:130px;height:44px;border:1.5px solid var(--white);border-radius:22px;color:var(--ink);font-size:14px;display:flex;align-items:center;justify-content:center}
.btn-white{left:1008px;top:90px;width:129px;height:44px;background:var(--white);border-radius:22px;color:var(--purple);font-size:14px;display:flex;align-items:center;justify-content:center;box-shadow:0 4px 14px rgba(0,0,0,.12)}

/* hero */
.hero-kicker{left:62px;top:308px;font-size:46px;font-weight:700;letter-spacing:14px}
.hero-kicker span:nth-child(1){color:#3b8ef2}.hero-kicker span:nth-child(2){color:#4a87f0}
.hero-kicker span:nth-child(3){color:#5a7ff0}.hero-kicker span:nth-child(4){color:#6b78f0}
.hero-kicker span:nth-child(5){color:#8a5cef}.hero-kicker span:nth-child(6){color:#a94be8}
.hero-kicker span:nth-child(7){color:#b94ae6}.hero-kicker span:nth-child(8){color:#c448e2}
.hero-title{left:62px;top:356px;font-size:50px;font-weight:500}
.hero-copy{left:62px;top:434px;width:440px;font-size:18px;line-height:24px;color:var(--gray)}
.btn-blue{background:var(--blue);color:var(--white);border-radius:28px;display:flex;align-items:center;justify-content:center;font-weight:600}
.hero-btn{left:61px;top:546px;width:193px;height:55px;font-size:15px;letter-spacing:1px}
.photo{border-radius:4px}

/* services */
.service{width:296px;height:296px;top:776px}
.service .shot{position:absolute;inset:0}
.service .tag{position:absolute;left:160px;top:86px;font-family:"Dancing Script",cursive;font-size:20px}
.service h3{position:absolute;left:160px;top:114px;font-size:19px;font-weight:700}
.service p{position:absolute;left:160px;top:146px;width:125px;font-size:12.5px;line-height:21px}
.service .book{position:absolute;left:210px;top:228px;width:95px;height:40px;background:#000;color:var(--white);font-size:13px;font-weight:600;display:flex;align-items:center;justify-content:center}

/* signature */
.sig-title{left:696px;top:1278px;font-size:34px;font-weight:700;line-height:41px}
.sig-lead{left:697px;top:1386px;width:390px;font-size:15.5px;font-weight:600;line-height:24px}
.sig-copy{left:697px;top:1446px;width:385px;font-size:14px;line-height:24px;color:#555}
.sig-btn{left:697px;top:1614px;width:160px;height:48px;font-size:13px;font-weight:500}

/* partners */
.partner{top:2293px;height:36px;border-radius:18px;background:#d9d9d9}

/* testimonials */
.section-title{left:0;width:1190px;top:2425px;text-align:center;font-size:34px;font-weight:700}
.card{top:2528px;width:295px;height:450px;background:var(--white);box-shadow:0 6px 24px rgba(0,0,0,.08);border-radius:3px;text-align:center}
.card.active{background:linear-gradient(160deg,#5fd0fb 0%,#3f8cf0 60%,#2f6fe4 100%);color:var(--ink)}
.card .ring{position:absolute;left:69px;top:20px;width:157px;height:157px;border-radius:50%;border:2px solid var(--blue-deep);display:flex;align-items:center;justify-content:center}
.card.active .ring{border-color:var(--white)}
.card .ring i{width:141px;height:141px;border-radius:50%;background:linear-gradient(#8a8580,#3c3a38)}
.card h4{position:absolute;left:0;right:0;top:205px;font-size:20px;font-weight:600;letter-spacing:3px}
.card p{position:absolute;left:22px;right:22px;top:240px;font-size:15px;line-height:21px;color:#555}
.card.active p{color:#1d2a4a}
.card .social{position:absolute;left:0;right:0;top:400px;display:flex;justify-content:center;gap:16px}
.card .social b{width:12px;height:12px;border-radius:50%;background:var(--blue-deep)}

/* cta */
.cta{left:137px;top:3105px;width:888px;height:230px;background:linear-gradient(100deg,var(--violet) 0%,#5a3fe0 50%,var(--blue-deep) 100%);text-align:center;color:var(--white)}
.cta h2{margin-top:48px;font-size:32px;line-height:40px;font-weight:700}
.cta .go{position:absolute;left:368px;top:150px;width:155px;height:45px;background:var(--white);color:var(--blue-deep);border-radius:23px;font-size:13px;font-weight:500;display:flex;align-items:center;justify-content:center}

/* footer */
.foot-brand{left:166px;top:3470px;font-size:30px;font-weight:700;color:var(--ink)}
.foot-info{left:136px;top:3528px;font-size:14.5px;line-height:21px;color:var(--white)}
.foot-phone{left:136px;top:3584px;font-size:15px;color:var(--white)}
.foot-social{left:137px;top:3630px;display:flex;gap:18px}
.foot-social b{width:12px;height:12px;border-radius:50%;background:var(--white)}
.foot-col{top:3448px;color:var(--white);font-size:14.5px}
.foot-col h5{font-size:15.5px;font-weight:600;margin-bottom:20px}
.foot-col li{list-style:none;height:36px}
.copy{left:0;width:1210px;top:3752px;text-align:center;color:var(--white);font-size:14.5px}
</style>
</head>
<body>

<!-- hero backdrop -->
<svg class="abs" style="left:0;top:0" width="1200" height="640" viewBox="0 0 1200 640">
  <defs>
    <linearGradient id="heroBlob" x1="0" y1="0" x2="1" y2="1">
      <stop offset="0" stop-color="#6fdcfb"/><stop offset=".55" stop-color="#4aa8f4"/><stop offset="1" stop-color="#2f74e6"/>
    </linearGradient>
    <linearGradient id="heroPurple" x1="0" y1="0" x2="1" y2="1">
      <stop offset="0" stop-color="#9b78f3"/><stop offset="1" stop-color="#3f7ff0"/>
    </linearGradient>
  </defs>
  <path d="M170 0 H1200 V580 C1140 560 1090 620 1020 600 C960 585 990 470 920 420 C860 380 760 420 700 360 C640 300 720 210 640 170 C560 130 500 180 420 150 C330 115 220 110 170 0Z" fill="url(#heroBlob)"/>
  <circle cx="520" cy="0" r="140" fill="#9be8fc" opacity=".8"/>
  <path d="M1020 0 H1200 V330 C1120 330 1020 270 1000 170 C985 90 1000 30 1020 0Z" fill="url(#heroPurple)"/>
  <circle cx="688" cy="259" r="30" fill="#fff"/>
  <circle cx="1023" cy="198" r="16" fill="#fff"/>
  <circle cx="627" cy="472" r="19" fill="#3f8cf0"/>
  <circle cx="998" cy="517" r="7" fill="#2f74e6"/>
</svg>

<div class="abs brand"><span class="dot"></span>Tailbrook</div>
<nav class="abs nav"><a>Locations</a><a>Careers</a><a>About</a><a>Blog</a><a>FAQ</a></nav>
<div class="abs btn-outline">Login</div>
<div class="abs btn-white">Signup</div>

<div class="abs hero-kicker"><span>D</span><span>O</span><span>O</span><span>R</span><span>S</span><span>T</span><span>E</span><span>P</span></div>
<h1 class="abs hero-title">Dog Grooming</h1>
<p class="abs hero-copy">Lorem ipsum dolor sit amet, consectetur dipiscing elit, sed do eiusmod tempor incididunt ut labore et dolore magna aliqua.</p>
<div class="abs btn-blue hero-btn">BOOK ONLINE</div>
<div class="abs photo" role="img" aria-label="Small shaggy dog wearing a blue patterned sweater" style="left:712px;top:215px;width:330px;height:400px;background:radial-gradient(ellipse at 50% 45%,#d9a36c 0%,#b98955 35%,#7fa8d6 70%,rgba(127,168,214,0) 100%)"></div>

<!-- services -->
<div class="abs service" style="left:118px">
  <div class="shot" role="img" aria-label="Long-haired hound on a yellow background" style="background:linear-gradient(90deg,#c8a070 0%,#f3b521 45%,#f7bd24 100%)"></div>
  <span class="tag" style="color:#fff">Best Services</span>
  <h3>Hair Care</h3>
  <p>Lorem ipsum dolor sit amet, sectetur adipiscing elit.</p>
  <div class="book">Book Now</div>
</div>
<div class="abs service" style="left:437px">
  <div class="shot" role="img" aria-label="Spotted dog shaking its paw, black and white" style="background:linear-gradient(90deg,#6d6d6d 0%,#cfcfcf 45%,#f2f2f2 100%)"></div>
  <span class="tag" style="color:#3f8cf0">Best Services</span>
  <h3>Nail Care</h3>
  <p>Lorem ipsum dolor sit amet, sectetur adipiscing elit.</p>
  <div class="book">Book Now</div>
</div>
<div class="abs service" style="left:757px">
  <div class="shot" role="img" aria-label="Fluffy black and white dog with a red bow" style="background:linear-gradient(90deg,#5a5a5e 0%,#e7e7ec 45%,#f3f3f7 100%)"></div>
  <span class="tag" style="color:#3f8cf0">Best Services</span>
  <h3>Breed Groom</h3>
  <p>Lorem ipsum dolor sit amet, sectetur adipiscing elit.</p>
  <div class="book">Book Now</div>
</div>

<!-- signature -->
<svg class="abs" style="left:0;top:1228px" width="620" height="440" viewBox="0 0 620 440">
  <defs><linearGradient id="arc" x1="0" y1="0" x2="1" y2="0"><stop offset="0" stop-color="#62d3fb"/><stop offset="1" stop-color="#3f8cf0"/></linearGradient></defs>
  <path d="M0 30 C180 10 360 20 450 120 C520 200 575 300 575 432 H0Z" fill="url(#arc)"/>
  <circle cx="452" cy="18" r="14" fill="#3f8cf0"/>
  <circle cx="550" cy="52" r="47" fill="#3f8cf0"/>
  <circle cx="586" cy="157" r="13" fill="#3f8cf0"/>
</svg>
<div class="abs" role="img" aria-label="Dog resting on a grey cushion bed under a blanket" style="left:0;top:1282px;width:575px;height:378px;border-top-right-radius:380px 360px;background:linear-gradient(180deg,#e8e6e2 0%,#c9c7c2 45%,#6f7f8f 70%,#a17a55 100%)"></div>
<h2 class="abs sig-title">The Furvanto<br>Signature Service</h2>
<p class="abs sig-lead">Lorem Ipsum is simply dummy text of the printing and typesetting industry.</p>
<p class="abs sig-copy">Lorem Ipsum is simply dummy text of the printing and typesetting industry. Lorem Ipsum has been the industry's standard dummy text ever since the 1500s, when an unknown printer took a galley of type and scrambled it to make a type specimen book. It has survived not only five centuries.</p>
<div class="abs btn-blue sig-btn" style="background:var(--blue-deep)">LEARN MORE</div>

<!-- video -->
<div class="abs" style="left:0;top:1790px;width:1136px;height:10px;background:linear-gradient(90deg,#62d3fb,#3f8cf0)"></div>
<div class="abs" role="img" aria-label="Two small dogs running along a sunlit dirt path" style="left:0;top:1800px;width:1200px;height:432px;background:linear-gradient(90deg,#8e7a63 0%,#c9ad8a 30%,#d8c1a0 55%,#a9a27f 80%,#7e8468 100%)"></div>
<svg class="abs" style="left:585px;top:1966px" width="86" height="100" viewBox="0 0 86 100"><path d="M0 0 L86 50 L0 100Z" fill="#2f6fe4"/></svg>
<div class="abs" style="left:62px;top:2232px;width:1138px;height:12px;background:linear-gradient(90deg,#3f8cf0,#62d3fb)"></div>

<!-- partners -->
<div class="abs partner" style="left:62px;width:142px"></div>
<div class="abs partner" style="left:239px;width:98px"></div>
<div class="abs partner" style="left:384px;width:104px"></div>
<div class="abs partner" style="left:527px;width:143px"></div>
<div class="abs partner" style="left:705px;width:144px"></div>
<div class="abs partner" style="left:891px;width:112px"></div>
<div class="abs partner" style="left:1037px;width:100px"></div>

<!-- testimonials -->
<svg class="abs" style="left:1030px;top:2365px" width="170" height="480" viewBox="0 0 170 480"><path d="M170 0 V480 C80 480 10 390 10 250 C10 110 80 10 170 0Z" fill="#b8a0f5"/></svg>
<h2 class="abs section-title">Testimonials</h2>
<svg class="abs" style="left:86px;top:2740px" width="26" height="26" viewBox="0 0 26 26"><path d="M24 13H4M12 4L3 13l9 9" stroke="#8c6cf2" stroke-width="3" fill="none"/></svg>
<svg class="abs" style="left:1083px;top:2740px" width="26" height="26" viewBox="0 0 26 26"><path d="M2 13h20M14 4l9 9-9 9" stroke="#3e20d8" stroke-width="3" fill="none"/></svg>

<div class="abs card active" style="left:131px">
  <div class="ring"><i role="img" aria-label="Portrait of a young woman"></i></div>
  <h4>JOHN DOE</h4>
  <p>Lorem ipsum dolor sit amet, consectetur adipiscing elit, sed do eiusmod tempor incididunt ut. Lorem ipsum dolor sit amet, consectetur adipiscing elit, sed do eiusmod tempor incididunt ut.</p>
  <div class="social"><b></b><b></b><b></b></div>
</div>
<div class="abs card" style="left:451px">
  <div class="ring"><i role="img" aria-label="Portrait of a bearded man"></i></div>
  <h4>LISA DAY</h4>
  <p>Lorem ipsum dolor sit amet, consectetur adipiscing elit, sed do eiusmod tempor incididunt ut. Lorem ipsum dolor sit amet, consectetur adipiscing elit, sed do eiusmod tempor incididunt ut.</p>
  <div class="social"><b></b><b></b></div>
</div>
<div class="abs card" style="left:771px">
  <div class="ring"><i role="img" aria-label="Portrait of a young woman with long hair"></i></div>
  <h4>JASON M.</h4>
  <p>Lorem ipsum dolor sit amet, consectetur adipiscing elit, sed do eiusmod tempor incididunt ut. Lorem ipsum dolor sit amet, consectetur adipiscing elit, sed do eiusmod tempor incididunt ut.</p>
  <div class="social"><b></b><b></b></div>
</div>

<!-- footer backdrop -->
<svg class="abs" style="left:0;top:3015px" width="1200" height="811" viewBox="0 0 1200 811">
  <defs><linearGradient id="footBg" x1="0" y1="0" x2="1" y2="1"><stop offset="0" stop-color="#4b96f3"/><stop offset="1" stop-color="#3a86f0"/></linearGradient></defs>
  <path d="M0 0 C90 10 160 90 180 188 H0Z" fill="#c9d6f6"/>
  <rect x="0" y="188" width="1200" height="623" fill="url(#footBg)"/>
  <path d="M0 700 C80 520 240 460 420 420 C600 380 760 460 900 500 C1040 540 1130 480 1200 440 V811 H0Z" fill="#5aa6f6" opacity=".45"/>
</svg>

<div class="abs cta">
  <h2>Already interested! Do you have any<br>project to working with?</h2>
  <div class="go">GET STARTED</div>
</div>

<div class="abs foot-brand">Tailbrook</div>
<p class="abs foot-info">Demo Addres avenue, street<br>12000, Country Name</p>
<p class="abs foot-phone">+123.456.789.000</p>
<div class="abs foot-social"><b></b><b></b><b></b><b></b></div>

<div class="abs foot-col" style="left:518px"><h5>Useful Link</h5><ul><li>Web Design</li><li>Development</li><li>Branding</li><li>Online Marketing</li><li>Content</li></ul></div>
<div class="abs foot-col" style="left:721px"><h5>About Us</h5><ul><li>About us</li><li>Work Portfolio</li><li>Team</li><li>Plan &amp; Pricing</li></ul></div>
<div class="abs foot-col" style="left:902px"><h5>Resources</h5><ul><li>Resources</li><li>News</li><li>API Docs</li><li>Help Center</li><li>Privacy &amp; Policy</li></ul></div>

<p class="abs copy">Copyright 2020 ©tailbrook</p>
</body>
</html>
```